Cosmetic injections clinic needs a fresh looking business card

We need a business card using the supplied logo and color scheme to attract future clients to our clinic. It should be modern and fresh, eye catching and not too busy. Simple and to the point is best. I would like two sided designs with the front indicating address and contact information, and the back in full color with white logo and descriptive information also provided.
Target Market(s)
Clients looking for non surgical beauty enhancements.
Contact Information for Business Card
Lumivela
14, 415 Carrow Ridge Road
St. Albert, Alberta
K2P 7W3
Phone: 431-662-0974
Email: info@lumivela-example.com
Requirements
Must have
- -Logo supplied with the name and address of the clinic
- -Back of card in full color with white logo with A small line of text indicating both of the following: Anti aging consultants and cosmetic injectables
- Located inside the Wayfarer Care Group

```html
<!DOCTYPE html>
<html lang="en">
<head>
<meta charset="utf-8">
<title>Lumivela — Business Card</title>
<link rel="stylesheet" href="https://fonts.googleapis.com/css2?family=Roboto:wght@400;500&display=swap">
<style>
  :root {
    --backdrop: #1d1b21;
    --card-white: #f4f4f5;
    --purple: #6a3fa0;
    --purple-deep: #4a2a7c;
    --purple-light: #7c55b3;
    --text-grey: #6d6b72;
    --white: #ffffff;
  }
  * { box-sizing: border-box; margin: 0; padding: 0; }
  html, body {
    width: 1200px; height: 1200px; overflow: hidden;
    background: var(--backdrop);
    font-family: "Roboto", Arial, sans-serif;
  }
  .sheet {
    width: 1200px; height: 1200px;
    display: flex; flex-direction: column; align-items: center; justify-content: center;
    gap: 60px;
  }
  .card {
    width: 840px; height: 480px; border-radius: 6px; position: relative; overflow: hidden;
    box-shadow: 0 18px 40px rgba(0,0,0,.55);
  }
  /* Front */
  .card--front { background: var(--card-white); padding: 60px 70px; }
  .brand-name {
    font-weight: 500; color: var(--purple); font-size: 64px; line-height: 1; letter-spacing: .5px;
  }
  .address { margin-top: 44px; color: var(--text-grey); font-size: 22px; line-height: 1.45; }
  .contact { margin-top: 18px; color: var(--text-grey); font-size: 22px; line-height: 1.6; }
  .contact-row { display: flex; align-items: center; gap: 12px; }
  .contact-row svg { width: 18px; height: 18px; fill: var(--purple); flex: none; }
  .tagline { margin-top: 26px; color: var(--text-grey); font-size: 21px; line-height: 1.45; }
  /* Back */
  .card--back {
    background: linear-gradient(160deg, var(--purple-deep) 0%, var(--purple) 60%, var(--purple-light) 100%);
    display: flex; align-items: center; justify-content: center;
  }
  .back-lockup { display: flex; align-items: center; gap: 26px; }
  .back-mark { width: 70px; height: 70px; border-radius: 50%; background: var(--white); }
  .back-name { font-weight: 500; color: var(--white); font-size: 84px; letter-spacing: 1px; }
</style>
</head>
<body>
<main class="sheet">
  <section class="card card--front" aria-label="Card front">
    <h1 class="brand-name">Lumivela</h1>
    <p class="address">14, 415 Carrow Ridge Road<br>St. Albert, Albert K2P 7W3</p>
    <div class="contact">
      <p class="contact-row">
        <svg viewBox="0 0 24 24" aria-hidden="true"><path d="M6.6 10.8a15.1 15.1 0 0 0 6.6 6.6l2.2-2.2c.3-.3.7-.4 1-.2 1.1.4 2.3.6 3.6.6.6 0 1 .4 1 1V20c0 .6-.4 1-1 1A17 17 0 0 1 3 4c0-.6.4-1 1-1h3.5c.6 0 1 .4 1 1 0 1.3.2 2.5.6 3.6.1.3 0 .7-.2 1z"/></svg>
        431-662-0974
      </p>
      <p class="contact-row">
        <svg viewBox="0 0 24 24" aria-hidden="true"><path d="M2 5h20v14H2z M2 5l10 8 10-8" fill="none" stroke="#6a3fa0" stroke-width="2"/><path d="M3 6l9 7 9-7v12H3z"/></svg>
        info@lumivela-example.com
      </p>
    </div>
    <p class="tagline">Anti aging consultants and cosmetic injectables<br>Located inside the Wayfarer Care Group</p>
  </section>

  <section class="card card--back" aria-label="Card back">
    <div class="back-lockup">
      <span class="back-mark" aria-hidden="true"></span>
      <span class="back-name">Lumivela</span>
    </div>
  </section>
</main>
</body>
</html>
```